Simple psychologist website
Open brief, creative designs encouraged
Site map:
Home
our services
our psychologists
selective mutism
resources
contact

Current website:
http://mindsproutyouth.com.au/
Not in love with our logo, or colours etc - open brief
Happy for new font/style/logo for company name - if we choose a logo design from a designer who doesn't win the competition, we will award $50 for the logo and use it in the new website

Website made a few years ago for a sister company that we really like:
http://www.korrelpsychology.com.au/

Clean, credible and warm and friendly look & feel
stock photos OK, designer will be required to hand over any images used in the design as shown in the PSD

Target Market(s)

Adolescents with psychological issues and their families

Industry/Entity Type

Psychology

Number of Pages Required

2 page

Colors

Designer to choose colors to be used in the design.

Requirements
Must have
• One home page - simple with 2 or 3 small areas to tease and attract the user and one template page to suit all the other pages
• We like slides, we want to have 3 slides like korrelpsychology.com.au
• Three slide titles:
• 1. We specialise in many areas, find the right clinical psychologist for your family
• 2. Child Clinical Psychologists in Chatswood and Westmead
• 3. Resources
• Pages structurally similar to
• http://www.korrelpsychology.com.au/
• We like the 'featured' items, which in our case will have splash box titles (can be 3 or 4):
• 1. Selective Mutism
• 2. Is my child anxious?
• 3. Does my child have an eating disorder?
• 4. Parenting adolescents
• Does not need to be a copy of http://www.korrelpsychology.com.au/ and we are willing to accept outside-the-box thinking and design (we in fact encourage it)
• Owner of business wants to highlight Selective Mutism as they have specialists. Consider ways that may make this work.
• Design winner will be based on home page design but winning designer will be required to provide an additional but simpler 'standard' page template design based on the themes used in the winning design.

```html
<!DOCTYPE html>
<html lang="en">
<head>
<meta charset="utf-8">
<title>MindSprout Youth – Clinical Psychologists</title>
<link href="https://fonts.googleapis.com/css2?family=Roboto:wght@400;500;700&display=swap" rel="stylesheet">
<style>
:root{
  --green:#6ab42d;
  --green-dark:#2f7d0b;
  --teal:#159b72;
  --orange:#f7931e;
  --blue:#1e90d8;
  --red:#ef3b3b;
  --ink:#222;
  --muted:#555;
  --grey-bg:#f2f2f2;
  --line:#ddd;
}
*{margin:0;padding:0;box-sizing:border-box}
html,body{width:864px;height:1200px;overflow:hidden}
body{font-family:"Roboto",Arial,sans-serif;color:var(--ink);background:#fff;position:relative}
.abs{position:absolute}
.brand{left:80px;top:20px;height:26px;padding:0 6px;background:var(--teal);color:#fff;font-weight:700;font-size:17px;line-height:26px;letter-spacing:.2px}
.nav{left:80px;top:67px;display:flex;list-style:none;font-size:12.5px}
.nav li{height:29px;line-height:29px;padding:0 12px;color:#333}
.nav li.active{background:var(--green);color:#fff;border-radius:2px 2px 0 0}
.nav-rule{left:0;top:96px;width:864px;height:2px;background:var(--green)}
.callbox{left:650px;top:0;width:134px;height:128px;color:#fff;text-align:center}
.callbox svg{position:absolute;left:0;top:0}
.callbox .inner{position:relative;padding-top:10px}
.callbox .ic{width:20px;height:20px;margin:0 auto 4px;border-radius:50%;background:#fff;display:flex;align-items:center;justify-content:center}
.callbox .l1{font-size:12px}
.callbox .num{font-size:17px;font-weight:500;margin:1px 0 2px}
.callbox .l3{font-size:12px;line-height:15px}
.hero{left:0;top:98px;width:864px;height:371px}
.hero-title{left:82px;top:210px;width:290px;color:#fff;font-weight:700;font-size:22px;line-height:25px}
.btn-white{left:80px;top:326px;width:79px;height:23px;border-radius:12px;background:#fff;color:#333;font-size:8.5px;line-height:23px;text-align:center}
.bubble{width:78px;height:78px;border-radius:50%;color:#fff;font-size:9.5px;line-height:12px;display:flex;align-items:center;justify-content:center;text-align:center}
.dots{left:80px;top:442px;display:flex;gap:3px}
.dots span{width:8px;height:8px;border-radius:50%;background:#555;opacity:.6}
.dots span:first-child{background:#fff;opacity:1}
.features{left:80px;top:488px;width:704px;display:flex;justify-content:space-between}
.feature{width:162px;text-align:center}
.feature .photo{height:110px;display:block}
.feature h3{font-weight:400;font-size:12.5px;line-height:16px;height:32px;margin-top:12px;display:flex;align-items:flex-start;justify-content:center}
.feature p{font-size:9.2px;line-height:15px;color:var(--muted);margin-top:14px;height:47px}
.btn-green{display:inline-block;margin-top:10px;width:79px;height:23px;border-radius:12px;background:var(--green);color:#fff;font-size:8.5px;line-height:23px}
.about{left:0;top:763px;width:864px;height:275px;background:var(--grey-bg)}
.about h2{position:absolute;left:80px;top:35px;width:350px;font-size:17px;font-weight:500;line-height:22px}
.about .lead{position:absolute;left:80px;top:100px;font-size:12px}
.about ul{position:absolute;left:80px;top:123px;width:342px;list-style:none;font-size:9.5px;color:#333}
.about li{padding:6px 0 6px 10px;border-bottom:1px solid var(--line);position:relative;line-height:15px}
.about li:last-child{border:none}
.about li::before{content:"›";position:absolute;left:0;top:5px;font-size:10px}
.about .photo{position:absolute;left:440px;top:36px;width:344px;height:204px}
.footer{left:0;top:1038px;width:864px;height:162px;background:var(--green-dark);color:#fff}
.footer .fbrand{position:absolute;left:80px;top:26px;height:22px;padding:0 5px;background:#fff;color:var(--green-dark);font-weight:700;font-size:15px;line-height:22px}
.footer .copy{position:absolute;left:80px;top:58px;font-size:9.5px;line-height:15px;color:#e4f0dc}
.footer .col{position:absolute;top:29px}
.footer h4{font-size:12.5px;font-weight:500;margin-bottom:5px}
.footer .col ul{list-style:none;font-size:9.5px;line-height:14.8px;color:#dfeed5}
.footer .callnote{position:absolute;left:620px;top:32px;font-size:9.5px;line-height:15px;display:flex;gap:4px}
.footer .social{position:absolute;left:622px;top:76px;width:33px;height:33px;background:#cfe3c2}
</style>
</head>
<body>
<div class="abs brand">MINDSPROUTYOUTH</div>
<ul class="abs nav">
  <li class="active">Home</li><li>Our Services</li><li>Our Psychologists</li><li>Selective Mutism</li><li>Resources</li><li>Contact</li>
</ul>
<div class="abs nav-rule"></div>

<section class="abs hero">
  <svg width="864" height="371" viewBox="0 0 864 371">
    <defs>
      <linearGradient id="photoTone" x1="0" y1="0" x2="1" y2="1">
        <stop offset="0" stop-color="#c9b27a"/><stop offset=".5" stop-color="#8a9a4a"/><stop offset="1" stop-color="#5f7a3a"/>
      </linearGradient>
      <linearGradient id="panelTone" x1="0" y1="0" x2="1" y2="1">
        <stop offset="0" stop-color="#7cc23a"/><stop offset="1" stop-color="#5aa62a"/>
      </linearGradient>
    </defs>
    <rect width="864" height="371" fill="url(#photoTone)" role="img" aria-label="Photo of a smiling family sitting together on grass in the sunshine"/>
    <path d="M0 0 H330 C375 5 378 80 372 150 C366 230 372 300 378 371 H0 Z" fill="url(#panelTone)"/>
    <path d="M330 0 C375 5 378 80 372 150" fill="none" stroke="#9fd46a" stroke-width="3" opacity=".6"/>
  </svg>
</section>
<div class="abs hero-title">We specialise in many areas, find the right clinical psychologist for your family</div>
<div class="abs btn-white">READ MORE</div>
<div class="abs bubble" style="left:418px;top:351px;background:var(--blue)">Selective<br>Mutism</div>
<div class="abs bubble" style="left:501px;top:375px;background:var(--orange)">Parenting<br>Adolescents</div>
<div class="abs bubble" style="left:586px;top:351px;background:var(--green)">Eating<br>disorders</div>
<div class="abs bubble" style="left:671px;top:372px;background:var(--red)">Child<br>Anxiety</div>
<div class="abs dots"><span></span><span></span><span></span></div>

<div class="abs callbox">
  <svg width="134" height="128" viewBox="0 0 134 128"><path d="M0 0 H134 V118 L67 128 L0 118 Z" fill="var(--orange)"/></svg>
  <div class="inner">
    <div class="ic"><svg width="12" height="12" viewBox="0 0 12 12"><path d="M3 1 L5 4 L4 5 C5 7 6 8 7 8 L8 7 L11 9 L10 11 C5 11 1 7 1 2 Z" fill="var(--orange)"/></svg></div>
    <div class="l1">Call Us On</div>
    <div class="num">0400 555 018</div>
    <div class="l3">for Chatswood &amp;<br>Westmead offices</div>
  </div>
</div>

<section class="abs features">
  <article class="feature">
    <div class="photo" role="img" aria-label="Photo of a psychologist talking with a young girl" style="background:linear-gradient(135deg,#e8e4df,#c9b9a8)"></div>
    <h3>Selective Mutism</h3>
    <p>Elena Novak, Clinical Psychologist at MindSprout Youth has many years of working with children.</p>
    <span class="btn-green">READ MORE</span>
  </article>
  <article class="feature">
    <div class="photo" role="img" aria-label="Photo of a worried boy sitting alone near a playground" style="background:linear-gradient(135deg,#8fa7c4,#4f6a3a)"></div>
    <h3>Is my child anxious?</h3>
    <p>Understanding childhood anxiety Anxiety is a normal and sometimes helpful emotion in all children.</p>
    <span class="btn-green">READ MORE</span>
  </article>
  <article class="feature">
    <div class="photo" role="img" aria-label="Photo of a teenage girl sitting in front of a plate of food" style="background:linear-gradient(135deg,#f3f1ee,#d8d2cc)"></div>
    <h3>Does my child have an eating disorder?</h3>
    <p>In summary, this article explains why eating disorders are dangerous and should be taken seriously.</p>
    <span class="btn-green">READ MORE</span>
  </article>
  <article class="feature">
    <div class="photo" role="img" aria-label="Photo of a mother and teenage daughter on a sofa" style="background:linear-gradient(135deg,#ece6de,#c4b39f)"></div>
    <h3>Parenting Adolescents</h3>
    <p>The way we think about sleep (and not sleeping) has a big impact on us. In particular, if your child.</p>
    <span class="btn-green">READ MORE</span>
  </article>
</section>

<section class="abs about">
  <h2>We are a group of clinical psychologists at Chatswood and Westmead (Sydney).</h2>
  <p class="lead">We provide a range of services including the following:</p>
  <ul>
    <li>Individual counselling and therapy for kids, teens and families</li>
    <li>Family consultatioans</li>
    <li>Seminars and training with schools</li>
    <li>Brief group programmes for anxiety, stress and body image concerns for adolescents</li>
  </ul>
  <div class="photo" role="img" aria-label="Photo of two teenagers running through an autumn park" style="background:linear-gradient(120deg,#d9a54a,#b86a2a 55%,#6d7f3a)"></div>
</section>

<footer class="abs footer">
  <div class="fbrand">MINDSPROUTYOUTH</div>
  <div class="copy">Copyright © 2017 MindSprout Youth.<br>All Rights Reserved.</div>
  <div class="col" style="left:291px">
    <h4>Quick Links</h4>
    <ul><li>Home</li><li>Our Services</li><li>Our Psychologists</li><li>Selective Mutism</li><li>Resources</li><li>Contact</li></ul>
  </div>
  <div class="col" style="left:415px">
    <h4>Information Links</h4>
    <ul><li>Areas of specialty</li><li>Making an appointment</li><li>Who can refer</li><li>What to expect at the first appointment</li><li>Handouts</li></ul>
  </div>
  <div class="callnote">
    <svg width="12" height="26" viewBox="0 0 12 26"><path d="M9 2 C3 2 2 8 2 13 C2 18 3 24 9 24" fill="none" stroke="#cfe3c2" stroke-width="1.3"/></svg>
    <span>Call us on 0400 555 018 for<br>Chatswood and Westmead offices</span>
  </div>
  <div class="social" aria-label="Social link"></div>
</footer>
</body>
</html>
```